Web Infographic for Life Insurance

We need an infographic for our insurance site based on research commissioned previously. We have a report of statistics on the cost and coverage of life insurance in 1999 vs 2019. What we're looking for is an infographic that presents these statistics in an entertaining and informative way. Site is CoverLantern.com
Target Market(s)
Americans ages 30-65 interested in life insurance.
Industry/Entity Type
Insurance
Number of Pages Required
1 page
Font styles to use
Sans Serif
Decorative
Colors
85cae6
faa54b
ffffff
86cfc6
Requirements
Must have
- Long vertical infographic readable on mobile devices
Nice to have
- Footnote references
Should not have
- Extremely small text
- Any brand logos or trademarked imagery other than for coverlantern

```html
<!DOCTYPE html>
<html lang="en">
<head>
<meta charset="utf-8">
<title>The Cost and Coverage of Life Insurance in 1999 vs 2019 | CoverLantern</title>
<link rel="stylesheet" href="https://fonts.googleapis.com/css2?family=Passion+One:wght@400;700&family=Oswald:wght@300;400&family=Poppins:wght@400;500;600;700&display=swap">
<style>
  :root {
    --sky: #85cae6;
    --sky-deep: #5fb6dc;
    --orange: #faa54b;
    --white: #ffffff;
    --mint: #86cfc6;
    --ink: #222428;
    --ink-soft: #4a4d52;
    --alert: #d0021b;
    --line: #d6e8f2;
    --footer: #444446;
  }
  * { box-sizing: border-box; margin: 0; padding: 0; }
  html, body { width: 1200px; height: 3878px; overflow: hidden; background: var(--white); }
  body { position: relative; font-family: "Poppins", sans-serif; color: var(--ink); }
  .abs { position: absolute; }

  /* header */
  .hero-bg { left: 0; top: 0; }
  .brand { left: 110px; top: 30px; font-family: "Poppins", sans-serif; font-weight: 500; font-size: 36px; color: var(--white); letter-spacing: -0.5px; }
  .hero-title { left: 110px; top: 148px; color: var(--white); }
  .hero-title .strong { display: block; font-family: "Passion One", sans-serif; font-weight: 700; font-size: 49px; line-height: 58px; letter-spacing: 1px; }
  .hero-title .light { display: block; font-family: "Oswald", sans-serif; font-weight: 300; font-size: 37px; line-height: 60px; letter-spacing: 2px; }
  .hero-art { left: 492px; top: 60px; width: 600px; height: 520px; border-radius: 50%;
    background: radial-gradient(circle at 50% 45%, #f4f7fa 0%, #e9eef3 55%, #ffffff 100%); }

  /* summary */
  .section-title { left: 0; width: 1200px; text-align: center; font-weight: 700; font-size: 32px; color: var(--ink); }
  .section-sub { left: 140px; width: 920px; text-align: center; font-size: 14px; line-height: 22px; color: var(--ink); }
  .blob { width: 145px; height: 148px; display: flex; align-items: center; justify-content: center; text-align: center;
    color: var(--white); font-weight: 500; font-size: 22px; line-height: 27px; }
  .blob.sky { background: var(--sky); border-radius: 58% 42% 50% 50% / 44% 50% 50% 56%; }
  .blob.orange { background: var(--orange); border-radius: 46% 54% 48% 52% / 56% 46% 54% 44%; }
  .stat-label { width: 340px; text-align: center; font-weight: 500; font-size: 23px; color: var(--ink); }
  .stat-label small { display: block; font-weight: 400; font-size: 17px; color: var(--ink-soft); margin-top: 2px; }
  .tag-box { left: 486px; top: 1209px; width: 226px; height: 127px; background: var(--white); border-radius: 8px;
    box-shadow: 0 3px 10px rgba(0,0,0,0.16); display: flex; align-items: center; justify-content: center; text-align: center;
    font-weight: 500; font-size: 23px; line-height: 40px; color: var(--ink); }
  .divider { left: 110px; top: 1433px; width: 980px; height: 2px; background: var(--line); }

  /* purchases */
  .side-note { left: 752px; width: 356px; top: 1640px; text-align: center; font-size: 14px; line-height: 22px; color: var(--ink); }
  .art-left { left: 101px; top: 1672px; width: 340px; height: 332px; background: radial-gradient(circle at 55% 50%, #dcebf6, #eef5fa 70%, #f6f9fc); border-radius: 48% 52% 46% 54%; }
  .art-map { left: 476px; top: 1732px; width: 254px; height: 226px; background: radial-gradient(circle, #cfe7d9, #e5f2f7 75%); border-radius: 50%; }
  .art-right { left: 760px; top: 1694px; width: 354px; height: 306px; background: radial-gradient(circle at 55% 55%, #0f86c9, #1992d3 60%, #2aa0dd); border-radius: 52% 48% 40% 60% / 56% 44% 56% 44%; }
  .finding { left: 184px; top: 2051px; width: 832px; height: 98px; background: var(--white); border-radius: 8px;
    box-shadow: 0 3px 10px rgba(0,0,0,0.14); display: flex; align-items: center; justify-content: center;
    text-align: center; padding: 0 40px; color: var(--alert); font-size: 17px; line-height: 23px; }

  /* cards */
  .card { top: 2241px; width: 457px; height: 527px; border-radius: 16px; border: 4px solid var(--white);
    box-shadow: 0 0 0 1px #e6e6e6, 0 3px 10px rgba(0,0,0,0.12); padding: 26px 18px 0 20px; color: var(--white); }
  .card.numbers { left: 112px; background: var(--orange); }
  .card.cost { left: 630px; background: var(--sky); }
  .card h3 { font-weight: 600; font-size: 26px; line-height: 30px; margin-bottom: 18px; }
  .card ul { list-style: none; }
  .card li { position: relative; padding-left: 28px; font-size: 16px; line-height: 25px; }
  .card li::before { content: "»"; position: absolute; left: 2px; top: 0; font-size: 16px; }

  /* chart */
  .chart { left: 0; top: 3040px; }

  /* footer */
  .footer-bg { left: 0; top: 3630px; }
  .copyright { left: 0; width: 1200px; top: 3812px; text-align: center; font-weight: 500; font-size: 17px; color: var(--white); }
</style>
</head>
<body>

<!-- header -->
<svg class="abs hero-bg" width="1200" height="720" viewBox="0 0 1200 720" aria-hidden="true">
  <path d="M0,0 H1200 V520 C1130,640 980,712 800,705 C560,695 420,560 220,530 C120,515 50,530 0,555 Z" fill="var(--sky)"/>
</svg>
<div class="abs brand">coverlantern</div>
<h1 class="abs hero-title">
  <span class="strong">THE COST AND</span>
  <span class="strong">COVERAGE OF</span>
  <span class="light">LIFE INSURANCE IN</span>
  <span class="light">1999 VS 2019</span>
</h1>
<div class="abs hero-art" role="img" aria-label="Illustration of a man beside a car, a house, a signed insurance document with a pen, and a heart with pills"></div>

<!-- summary statistics -->
<h2 class="abs section-title" style="top:826px;">SUMMARY STATISTICS (1992-1997)</h2>
<p class="abs section-sub" style="top:884px;">There's a lot to consider when choosing the right Health Insurance coverage. CoverLantern prides itself with our custom ratings and reviews.</p>

<svg class="abs" style="left:0;top:940px;" width="1200" height="200" viewBox="0 940 1200 200" aria-hidden="true">
  <g fill="none" stroke="#222" stroke-width="2" stroke-dasharray="5 5">
    <path d="M123,1098 C110,1060 130,1020 165,1030 C185,1036 195,1045 210,1050"/>
    <path d="M352,1062 C385,1055 410,1045 432,1036"/>
    <path d="M462,1030 C480,1028 505,1028 525,1040"/>
    <path d="M663,1100 C700,1108 735,1110 762,1108"/>
    <path d="M795,1102 C815,1092 835,1080 851,1072"/>
    <path d="M985,1035 C1030,1020 1060,995 1080,970"/>
  </g>
  <circle cx="123" cy="1098" r="7" fill="#222"/>
  <path d="M425,1030 L458,1028 L438,1050 Z" fill="#fff" stroke="#222" stroke-width="2" stroke-linejoin="round"/>
  <path d="M760,1100 L792,1102 L770,1122 Z" fill="#fff" stroke="#222" stroke-width="2" stroke-linejoin="round"/>
  <path d="M1072,978 L1085,958 L1062,962" fill="none" stroke="#222" stroke-width="2.5" stroke-linejoin="round"/>
</svg>

<div class="abs blob sky" style="left:207px;top:988px;">3.62 {4.91}</div>
<div class="abs blob orange" style="left:526px;top:988px;">2.27</div>
<div class="abs blob sky" style="left:855px;top:988px;">132.97<br>{136.41}</div>

<div class="abs stat-label" style="left:112px;top:1152px;">Type Term Premium<small>($ 1000. of face)</small></div>
<div class="abs stat-label" style="left:430px;top:1152px;">Length of policy</div>
<div class="abs stat-label" style="left:761px;top:1152px;">Real Amount of Policy<small>(in 000s of 1990 dollars)</small></div>
<div class="abs tag-box">Non-Smoker<br>Male</div>

<div class="abs divider"></div>

<!-- purchases -->
<h2 class="abs section-title" style="top:1516px;line-height:44px;">Number of life insurance policy purchases in the United<br>States from 1998 to 2018 (in millions)</h2>
<p class="abs side-note">In 2018, approximately 27.8 million life insurance policies were purchased in the United States.</p>

<div class="abs art-left" role="img" aria-label="Illustration of people around a large health insurance form under an umbrella"></div>
<div class="abs art-map" role="img" aria-label="Illustration of a colourful map of the United States"></div>
<div class="abs art-right" role="img" aria-label="Illustration of a growth chart with a rising arrow and a magnifying glass"></div>

<svg class="abs" style="left:400px;top:1700px;" width="420" height="80" viewBox="0 0 420 80" aria-hidden="true">
  <g fill="none" stroke="#111" stroke-width="3" stroke-linecap="round" stroke-linejoin="round">
    <path d="M14,32 C40,8 80,6 104,30"/>
    <path d="M92,30 L105,32 L104,18"/>
    <path d="M298,30 C325,6 365,6 388,30"/>
    <path d="M376,30 L389,32 L388,18"/>
  </g>
</svg>

<div class="abs finding">The results suggest that the growth of the Internet has reduced term life prices by 8–15 percent.</div>

<!-- cards -->
<section class="abs card numbers">
  <h3>Life Insurance By The Numbers</h3>
  <ul>
    <li>57%&nbsp; Percent of American adults who have life in surance</li>
    <li>32% Of American adults with life insurance, the percent who only have group coverage — which usually isn't enough (and is rarely por table)</li>
    <li>10x to 12x&nbsp; The multiples of your annual income that most financial advisors recommend you need when buying life insurance for income replacement</li>
    <li>50% Percent of life insurance policies are pur chased via independent agents</li>
    <li>40% Percent of life insurance policies purchased via affiliated agents (meaning they only sell products for one insurance company)</li>
  </ul>
</section>

<section class="abs card cost">
  <h3>Stats about the cost of life insurance</h3>
  <ul>
    <li>6x-10x How much more permanent life insurance (like whole life insurance) costs vs. term life insurance</li>
    <li>8% * Average percent increase in your insurance costs as you age, assuming your health stays the same</li>
    <li>30% The average cost difference between sequen tial health ratings (preferred vs standard, for example)</li>
    <li>2x to 3x How much rates for smokers cost vs. rates for nonsmokers (but a year after you quit smoking, most companies will offer you non smoker rates)</li>
    <li>50% The average difference between the least ex pensive and most expensive rate for the same person across insurance companies</li>
  </ul>
</section>

<!-- reasons chart -->
<h2 class="abs section-title" style="top:2902px;">Top reasons for buying life insurance in the U.S.</h2>
<p class="abs section-sub" style="top:2960px;left:130px;width:940px;">According to a 2019 report from trade research organization Ledgerline Research and the non-profit organization Cover Ahead, these are the most common reasons Americans said they bought life insurance:</p>

<svg class="abs chart" width="1200" height="560" viewBox="0 3040 1200 560" role="img" aria-label="Bar chart of top reasons for buying life insurance">
  <g stroke="#222" stroke-width="1.5">
    <line x1="142" y1="3062" x2="142" y2="3516"/>
    <line x1="142" y1="3516" x2="1100" y2="3516"/>
    <line x1="130" y1="3108" x2="142" y2="3108"/><line x1="130" y1="3149" x2="142" y2="3149"/>
    <line x1="130" y1="3190" x2="142" y2="3190"/><line x1="130" y1="3230" x2="142" y2="3230"/>
    <line x1="130" y1="3271" x2="142" y2="3271"/><line x1="130" y1="3312" x2="142" y2="3312"/>
    <line x1="130" y1="3353" x2="142" y2="3353"/><line x1="130" y1="3394" x2="142" y2="3394"/>
    <line x1="130" y1="3435" x2="142" y2="3435"/><line x1="130" y1="3475" x2="142" y2="3475"/>
  </g>
  <g font-family="Poppins, sans-serif" font-size="15" fill="#222" text-anchor="end">
    <text x="122" y="3113">100</text><text x="122" y="3154">90</text><text x="122" y="3195">80</text>
    <text x="122" y="3235">70</text><text x="122" y="3276">60</text><text x="122" y="3317">50</text>
    <text x="122" y="3358">40</text><text x="122" y="3399">30</text><text x="122" y="3440">20</text>
    <text x="122" y="3480">10</text>
  </g>
  <g>
    <rect x="155" y="3365" width="33" height="151" fill="var(--sky)"/>
    <rect x="253" y="3394" width="33" height="122" fill="var(--orange)"/>
    <rect x="336" y="3402" width="33" height="114" fill="var(--sky)"/>
    <rect x="410" y="3406" width="33" height="110" fill="var(--orange)"/>
    <rect x="500" y="3438" width="33" height="78" fill="var(--sky)"/>
    <rect x="606" y="3447" width="33" height="69" fill="var(--orange)"/>
    <rect x="697" y="3459" width="33" height="57" fill="var(--sky)"/>
    <rect x="768" y="3459" width="33" height="57" fill="var(--orange)"/>
    <rect x="851" y="3463" width="33" height="53" fill="var(--sky)"/>
    <rect x="941" y="3483" width="33" height="33" fill="var(--orange)"/>
    <rect x="1033" y="3483" width="33" height="33" fill="var(--sky)"/>
  </g>
  <g font-family="Poppins, sans-serif" font-size="14" fill="#555" text-anchor="middle">
    <text x="172" y="3352">37%</text><text x="270" y="3381">30%</text><text x="352" y="3389">28%</text>
    <text x="427" y="3393">27%</text><text x="517" y="3425">19%</text><text x="622" y="3434">17%</text>
    <text x="714" y="3446">14%</text><text x="785" y="3446">14%</text><text x="868" y="3450">13%</text>
    <text x="958" y="3470">8%</text><text x="1050" y="3470">8%</text>
  </g>
  <g font-family="Poppins, sans-serif" font-size="13" fill="#222">
    <text x="145" y="3544">Income</text><text x="145" y="3563">replacement</text>
    <text x="243" y="3544">Burial/final</text><text x="243" y="3563">expenses</text>
    <text x="333" y="3544">Wealth</text><text x="333" y="3563">transfer</text>
    <text x="405" y="3544">Pay off</text><text x="405" y="3563">mortgage</text>
    <text x="486" y="3544">Replaced a</text><text x="486" y="3563">policy</text>
    <text x="577" y="3544">Tax advantaged</text><text x="577" y="3563">save/invest</text>
    <text x="699" y="3544">Estate</text><text x="699" y="3563">taxes</text>
    <text x="760" y="3544">Funds for</text><text x="760" y="3563">college</text><text x="760" y="3582">education</text>
    <text x="842" y="3544">Charitable</text><text x="842" y="3563">gift</text>
    <text x="923" y="3544">Supplement</text><text x="923" y="3563">group</text><text x="923" y="3582">coverage</text>
    <text x="1020" y="3544">Business</text><text x="1020" y="3563">purposes</text>
  </g>
</svg>

<!-- footer -->
<svg class="abs footer-bg" width="1200" height="248" viewBox="0 3630 1200 248" aria-hidden="true">
  <path d="M0,3720 C20,3680 60,3656 130,3654 C500,3660 900,3690 1200,3720 V3878 H0 Z" fill="var(--footer)"/>
</svg>
<p class="abs copyright">Copyrights @ 2020 Coverlantern. All Rights Reserved.</p>

</body>
</html>
```